Banner Designs for Drone Defense Ad Campaign

Corvane is a security consulting and services company that offers a service called SkyMindful. SkyMindful helps our customers identify security risks from drones and develops comprehensive protection programs. We are looking for a designer to create a banner ad in three sizes for our campaign.
Target Market(s)
Our campaign is geared to the sports and entertainment industry, specifically large event venues and their security operation.
Industry/Entity Type
Security
Font styles to use
Other font styles liked:
- Raleway
Requirements
Must have
- Banner Objective
The visual and textual content of the banner should prompt the viewer to quickly identify the service offered and the information that is available to download.
Banner Design
Logo: SkyMindful logo
Call to Action Button in Red: Get It Here (On Right or or Upper Right)
Title in Larger Font: Guide to UAS Risk Mitigation
Subtitle in smaller Font: 5 Steps to Develop Your Comprehensive UAS Defense Program
Background: Stadium with a drone flying in foreground
Font: Raleway
Banner Sizes
1 - 1200x670 pixels
2 - 1510x196 pixels
3 - 1200x628 pixels

```html
<!DOCTYPE html>
<html lang="en">
<head>
<meta charset="utf-8">
<title>Banner Designs for Drone Defense Ad Campaign</title>
<link rel="stylesheet" href="https://fonts.googleapis.com/css2?family=Raleway:wght@300;400;500;800;900&display=swap">
<style>
  :root {
    --sheet-grey: #b3b3b3;
    --ink: #1d1d1d;
    --night: #03050f;
    --brand-blue: #2f84d8;
    --white: #ffffff;
    --cta-red: #d40000;
    --logo-grey: #9a9a9a;
  }
  * { box-sizing: border-box; margin: 0; padding: 0; }
  html, body {
    width: 927px; height: 1200px; overflow: hidden;
    background: var(--sheet-grey);
    font-family: "Raleway", sans-serif;
  }
  .sheet { position: relative; width: 927px; height: 1200px; }
  .sheet-title {
    position: absolute; top: 56px; left: 0; width: 927px;
    text-align: center; font-weight: 400; font-size: 25px; color: var(--ink);
  }
  .sample-label {
    position: absolute; left: 62px; font-size: 16px; font-weight: 400; color: var(--ink);
  }
  .sample-label--one { top: 121px; }
  .sample-label--two { top: 651px; }

  .banner {
    position: absolute; left: 62px; width: 803px; height: 449px;
    background: var(--night); overflow: hidden;
    box-shadow: 0 3px 6px rgba(0,0,0,.35);
  }
  .banner--one { top: 156px; }
  .banner--two { top: 686px; }

  .banner-photo { position: absolute; inset: 0; }
  .banner--one .banner-photo {
    background:
      linear-gradient(90deg, var(--night) 0%, var(--night) 38%, rgba(3,5,15,.6) 52%, rgba(3,5,15,0) 66%),
      radial-gradient(ellipse 45% 55% at 78% 68%, #5fa132 0%, #3f7d22 45%, rgba(30,50,20,0) 75%),
      linear-gradient(180deg, #141a16 0%, #2b3a2a 30%, #2f4a22 60%, #1b2a14 100%);
  }
  .banner--two .banner-photo {
    background:
      linear-gradient(90deg, var(--night) 0%, var(--night) 30%, rgba(3,5,15,.55) 48%, rgba(3,5,15,0) 62%),
      radial-gradient(ellipse 42% 28% at 72% 86%, #5b3e9c 0%, #2e2f6a 50%, rgba(20,25,60,0) 80%),
      linear-gradient(180deg, #2b2234 0%, #c88a5a 13%, #e9b26f 19%, #2a3550 30%, #17233d 55%, #0c1428 100%);
  }

  .brand { position: absolute; left: 34px; top: 34px; width: 260px; }
  .brand-name {
    display: flex; align-items: center; gap: 10px;
    font-size: 32px; font-weight: 500; color: var(--brand-blue); line-height: 1;
  }
  .brand-dot { width: 14px; height: 14px; border-radius: 50%; background: var(--logo-grey); }
  .brand-byline {
    margin-top: 6px; text-align: right; padding-right: 16px;
    font-size: 19px; font-weight: 500; color: var(--white);
  }

  .headline { position: absolute; left: 48px; top: 152px; }
  .headline-lead {
    font-size: 50px; font-weight: 300; color: var(--white); line-height: 1; letter-spacing: -0.5px;
  }
  .headline-main {
    margin-top: 2px;
    font-size: 68px; font-weight: 900; color: var(--brand-blue); line-height: 0.92; letter-spacing: -1px;
  }
  .subtitle {
    position: absolute; left: 48px; top: 350px;
    font-size: 16.5px; font-weight: 500; color: var(--white); line-height: 26px;
  }

  .cta { position: absolute; top: 0; right: 0; width: 151px; height: 137px; }
  .cta-band { fill: var(--cta-red); }
  .cta-text {
    fill: var(--white); font-family: "Raleway", sans-serif; font-weight: 900; font-size: 25px;
  }
</style>
</head>
<body>
<main class="sheet">
  <h1 class="sheet-title">Banner Designs for Drone Defense Ad Campaign</h1>

  <p class="sample-label sample-label--one">Sample 1</p>
  <section class="banner banner--one">
    <div class="banner-photo" role="img" aria-label="Aerial night view of a floodlit football stadium with a white quadcopter drone hovering above the crowd"></div>
    <div class="brand">
      <div class="brand-name"><span class="brand-dot"></span>SkyMindful</div>
      <div class="brand-byline">By Corvane</div>
    </div>
    <h2 class="headline">
      <span class="headline-lead">GUIDE TO</span><br>
      <span class="headline-main">UAS RISK<br>MITIGATION</span>
    </h2>
    <p class="subtitle">5 Steps to Develop Your Comprehensive<br>UAS Defense Program</p>
    <svg class="cta" viewBox="0 0 151 137" aria-label="Get it here">
      <polygon class="cta-band" points="0,0 94,0 151,58 151,137"/>
      <g transform="translate(100 50) rotate(42)">
        <text class="cta-text" x="0" y="-4" text-anchor="middle">GET IT</text>
        <text class="cta-text" x="0" y="20" text-anchor="middle">HERE</text>
      </g>
    </svg>
  </section>

  <p class="sample-label sample-label--two">Sample 2</p>
  <section class="banner banner--two">
    <div class="banner-photo" role="img" aria-label="Sunset aerial view over a city with a lit oval stadium and a white quadcopter drone flying in the foreground"></div>
    <div class="brand">
      <div class="brand-name"><span class="brand-dot"></span>SkyMindful</div>
      <div class="brand-byline">By Corvane</div>
    </div>
    <h2 class="headline">
      <span class="headline-lead">GUIDE TO</span><br>
      <span class="headline-main">UAS RISK<br>MITIGATION</span>
    </h2>
    <p class="subtitle">5 Steps to Develop Your Comprehensive<br>UAS Defense Program</p>
    <svg class="cta" viewBox="0 0 151 137" aria-label="Get it here">
      <polygon class="cta-band" points="0,0 94,0 151,58 151,137"/>
      <g transform="translate(100 50) rotate(42)">
        <text class="cta-text" x="0" y="-4" text-anchor="middle">GET IT</text>
        <text class="cta-text" x="0" y="20" text-anchor="middle">HERE</text>
      </g>
    </svg>
  </section>
</main>
</body>
</html>
```